Pinecrest Lockworks Business Card Design

Double Sided Business Card Design for a Locksmith company specializing in Safecracking, safe & vault service.

```html
<!DOCTYPE html>
<html lang="en">
<head>
<meta charset="utf-8">
<title>Pinecrest Lockworks Business Card</title>
<link rel="stylesheet" href="https://fonts.googleapis.com/css2?family=Montserrat:wght@400;500;700;800&display=swap">
<style>
  :root {
    --green: #2e8a45;
    --green-deep: #267a3b;
    --green-pattern: #236f36;
    --paper: #ffffff;
    --ink: #4a4a4a;
    --ink-soft: #6b6b6b;
    --faint: #e6e7e8;
    --stage: #d9d9d9;
  }
  * { box-sizing: border-box; margin: 0; padding: 0; }
  html, body { width: 1200px; height: 675px; overflow: hidden; }
  body {
    background: var(--stage);
    font-family: "Montserrat", Arial, sans-serif;
    display: flex;
    align-items: center;
    justify-content: center;
    gap: 48px;
  }
  .card {
    width: 525px;
    height: 300px;
    border-radius: 16px;
    position: relative;
    overflow: hidden;
    box-shadow: 0 10px 24px rgba(0,0,0,0.18);
  }

  /* Back side */
  .card-back { background: var(--green); }
  .back-pattern {
    position: absolute; inset: 0;
    background: linear-gradient(120deg, var(--green-pattern) 0%, var(--green) 45%, var(--green-deep) 100%);
    opacity: 0.9;
  }
  .back-brand {
    position: absolute;
    left: 300px; top: 186px;
    display: flex; align-items: center; gap: 10px;
    color: var(--paper);
  }
  .brand-dot {
    width: 34px; height: 34px; border-radius: 50%;
    flex: none;
  }
  .back-brand .brand-dot { background: var(--paper); }
  .brand-name {
    font-weight: 800;
    font-size: 19px;
    line-height: 1.05;
    letter-spacing: 0.5px;
    text-transform: uppercase;
  }

  /* Front side */
  .card-front { background: var(--paper); }
  .front-backdrop {
    position: absolute;
    left: 0; top: 40px;
    width: 230px; height: 170px;
    background: radial-gradient(ellipse at 40% 50%, var(--faint) 0%, rgba(230,231,232,0.5) 55%, rgba(255,255,255,0) 80%);
  }
  .front-brand {
    position: absolute;
    left: 26px; top: 24px;
    display: flex; align-items: center; gap: 10px;
    color: var(--green);
  }
  .front-brand .brand-dot { background: var(--green); width: 30px; height: 30px; }
  .front-brand .brand-name { font-size: 17px; }

  .contact {
    position: absolute;
    left: 210px; top: 150px;
    padding-left: 14px;
    border-left: 2px solid var(--green);
    list-style: none;
    color: var(--ink);
    font-size: 11.5px;
    font-weight: 500;
    line-height: 1.35;
  }
  .contact li { display: flex; align-items: flex-start; gap: 7px; margin-bottom: 3px; }
  .contact svg { width: 11px; height: 11px; flex: none; margin-top: 2px; fill: var(--green); }

  .person {
    position: absolute;
    right: 40px; top: 64px;
    text-align: center;
  }
  .person-name {
    color: var(--green);
    font-weight: 700;
    font-size: 26px;
    letter-spacing: 0.5px;
  }
  .person-role {
    color: var(--ink-soft);
    font-size: 12px;
    font-weight: 400;
  }
</style>
</head>
<body>

  <section class="card card-back" aria-label="Business card back">
    <div class="back-pattern" role="img" aria-label="Repeating tonal green emblem pattern across the card"></div>
    <div class="back-brand">
      <span class="brand-dot"></span>
      <span class="brand-name">Pinecrest<br>Lockworks</span>
    </div>
  </section>

  <section class="card card-front" aria-label="Business card front">
    <div class="front-backdrop" role="img" aria-label="Large faint grey brand emblem in the background"></div>
    <div class="front-brand">
      <span class="brand-dot"></span>
      <span class="brand-name">Pinecrest<br>Lockworks</span>
    </div>

    <ul class="contact">
      <li>
        <svg viewBox="0 0 12 12" aria-hidden="true"><path d="M6 0a4 4 0 0 0-4 4c0 3 4 8 4 8s4-5 4-8a4 4 0 0 0-4-4zm0 5.6A1.6 1.6 0 1 1 6 2.4a1.6 1.6 0 0 1 0 3.2z"/></svg>
        <span>4820 Maple Ridge Ave.<br>Suite 210, Pinecrest, TX 75301</span>
      </li>
      <li>
        <svg viewBox="0 0 12 12" aria-hidden="true"><path d="M2.4 0.6l2 2-1 1.4a7 7 0 0 0 4.6 4.6l1.4-1 2 2-1.4 1.8C5.6 11.4 0.6 6.4 0.6 2z"/></svg>
        <span>555-210-4837</span>
      </li>
      <li>
        <svg viewBox="0 0 12 12" aria-hidden="true"><path d="M0 2h12v8H0zm1 1v.4l5 3.2 5-3.2V3z"/></svg>
        <span>hello@pinecrestlockworks.com</span>
      </li>
      <li>
        <svg viewBox="0 0 12 12" aria-hidden="true"><circle cx="6" cy="6" r="5.5"/></svg>
        <span>pinecrestlockworks.com</span>
      </li>
    </ul>

    <div class="person">
      <div class="person-name">NAME</div>
      <div class="person-role">Designation</div>
    </div>
  </section>

</body>
</html>
```